Sign Design for Truck Repair Shop center

Need a road-side sign for a pickup truck repair shop called HaulPoint Garage. The logo is attached and should be used on the sign. The background should be white and the main part of the logo should take up a large part of the sign so it can be easily read by passing traffic. The sign is 4 feet tall by 8 feet wide. Also need to add the website address" "www.HaulPointGarage-example.com" and "Call/Text 555.382.4607"

```html
<!DOCTYPE html>
<html lang="en">
<head>
<meta charset="utf-8">
<title>HaulPoint Garage – Roadside Sign</title>
<link rel="stylesheet" href="https://fonts.googleapis.com/css2?family=Arvo:wght@400;700&family=Montserrat:wght@500&display=swap">
<style>
  :root {
    --brand-blue: #0c57a2;
    --sign-white: #ffffff;
    --pattern-tone: #f2f3f5;
    --accent-grey: #c6c7c9;
  }
  * { margin: 0; padding: 0; box-sizing: border-box; }
  html, body { width: 1200px; height: 600px; overflow: hidden; background: var(--sign-white); }
  .sign { position: relative; width: 1200px; height: 600px; overflow: hidden; background: var(--sign-white); }
  .tool-pattern {
    position: absolute; inset: 0 0 auto 0; height: 280px;
    background: linear-gradient(180deg, var(--sign-white) 0%, var(--pattern-tone) 100%);
  }
  .sign-panels { position: absolute; inset: 0; }
  .shop-name {
    position: absolute; top: 78px; left: 0; width: 100%;
    text-align: center; font-family: "Arvo", serif; font-weight: 700;
    font-size: 86px; letter-spacing: 2px; text-transform: uppercase;
    color: var(--brand-blue); line-height: 1;
  }
  .tagline {
    position: absolute; top: 282px; left: 0; width: 100%;
    text-align: center; font-family: "Arvo", serif; font-weight: 700;
    font-size: 28px; letter-spacing: 2px; text-transform: uppercase;
    color: var(--sign-white);
  }
  .rating-stars { position: absolute; top: 352px; left: 510px; }
  .contact-line {
    position: absolute; top: 400px; left: 0; width: 100%;
    display: flex; justify-content: center; align-items: baseline; gap: 28px;
    color: var(--sign-white);
  }
  .contact-label { font-family: "Arvo", serif; font-weight: 700; font-size: 50px; letter-spacing: 3px; }
  .contact-phone { font-family: "Montserrat", sans-serif; font-weight: 500; font-size: 84px; letter-spacing: 1px; }
  .website-line {
    position: absolute; top: 515px; left: 0; width: 100%;
    display: flex; justify-content: center; align-items: center; gap: 14px;
    color: var(--sign-white);
  }
  .website { font-family: "Arvo", serif; font-weight: 400; font-size: 27px; letter-spacing: 4px; text-transform: uppercase; }
</style>
</head>
<body>
<div class="sign">
  <div class="tool-pattern" role="img" aria-label="Faint repeating pattern of wrenches, hammers, screwdrivers, hard hats and gears"></div>

  <svg class="sign-panels" width="1200" height="600" viewBox="0 0 1200 600" aria-hidden="true">
    <polygon points="0,269 281,226 919,226 1200,269" fill="var(--accent-grey)"/>
    <polygon points="0,269 281,252 600,238 919,252 1200,269 1200,600 0,600" fill="var(--brand-blue)"/>
  </svg>

  <div class="shop-name">HaulPoint Garage</div>
  <div class="tagline">Your Trusted Torvan Specialists</div>

  <svg class="rating-stars" width="180" height="46" viewBox="0 0 180 46" aria-label="Five stars" role="img">
    <g fill="var(--sign-white)">
      <polygon points="12,16 14.6,21.5 20.5,22 16,26 17.3,32 12,29 6.7,32 8,26 3.5,22 9.4,21.5"/>
      <polygon points="46,10 49.5,17.5 57.5,18.3 51.5,23.8 53.2,31.8 46,27.7 38.8,31.8 40.5,23.8 34.5,18.3 42.5,17.5"/>
      <polygon points="90,2 95.3,13.3 107.5,14.5 98.4,22.8 101,35 90,28.7 79,35 81.6,22.8 72.5,14.5 84.7,13.3"/>
      <polygon points="134,10 137.5,17.5 145.5,18.3 139.5,23.8 141.2,31.8 134,27.7 126.8,31.8 128.5,23.8 122.5,18.3 130.5,17.5"/>
      <polygon points="168,16 170.6,21.5 176.5,22 172,26 173.3,32 168,29 162.7,32 164,26 159.5,22 165.4,21.5"/>
    </g>
  </svg>

  <div class="contact-line">
    <span class="contact-label">CALL/TEXT</span>
    <span class="contact-phone">555.382.4607</span>
  </div>

  <div class="website-line">
    <svg width="90" height="14" viewBox="0 0 90 14" aria-hidden="true">
      <g fill="var(--sign-white)">
        <polygon points="0,3 90,1.5 90,3.5"/>
        <rect x="42" y="6" width="48" height="2"/>
        <polygon points="0,11 90,10.5 90,12.5"/>
      </g>
    </svg>
    <span class="website">www.HaulPointGarage-example.com</span>
    <svg width="90" height="14" viewBox="0 0 90 14" aria-hidden="true">
      <g fill="var(--sign-white)">
        <polygon points="90,3 0,1.5 0,3.5"/>
        <rect x="0" y="6" width="48" height="2"/>
        <polygon points="90,11 0,10.5 0,12.5"/>
      </g>
    </svg>
  </div>
</div>
</body>
</html>
```